Medical equipment business looking for professional, unique business card

We need a business card design for a durable medical equipment company. We are small but would like our cards to express that we are much bigger. We focus on braces (back, knee, wrist, etc) but also do crutches, rollators, wheelchairs- basically medical equipment that gets you going and back in Action. Our colors are blue and green and our logo has an arrow and use of a "spine". We'd like to express professionalism while being unique.

Industry/Entity Type

Medical Equipment

Contact Information for Business Card

Professional feel but unique. Memorable.

Font styles to use
Serif
Sans Serif
Other font styles liked:
• verdana

Requirements
Must have
• card holders cell#, business phone#, fax#, email, website address, business address, logo
Nice to have
• use of medical/healthcare related descriptive words, items, look
Should not have
• the wrong colors or cartoon characters.

```html
<!DOCTYPE html>
<html lang="en">
<head>
<meta charset="utf-8">
<title>Stride DME business card</title>
<link rel="stylesheet" href="https://fonts.googleapis.com/css2?family=Roboto:wght@400;500;700&display=swap">
<style>
  :root {
    --navy: #0d3a5c;
    --green: #7ab532;
    --ink: #1d3550;
    --paper: #f7f7f6;
    --backdrop: #e4e4e3;
    --rule: #d2d4d6;
  }
  * { margin: 0; padding: 0; box-sizing: border-box; }
  html, body {
    width: 1200px; height: 576px; overflow: hidden;
    background: var(--backdrop);
    font-family: "Roboto", Arial, sans-serif;
  }
  .canvas { position: relative; width: 1200px; height: 576px; }
  .card {
    position: absolute;
    width: 484px; height: 293px;
    background: var(--paper);
    border-radius: 6px;
    box-shadow: 0 2px 4px rgba(0,0,0,0.18);
    overflow: hidden;
  }
  .card--front { left: 82px; top: 139px; }
  .card--back { left: 600px; top: 138px; }

  .brand {
    position: absolute;
    display: flex; align-items: center;
    color: var(--navy);
    font-weight: 500;
    white-space: nowrap;
  }
  .brand__dot { border-radius: 50%; background: var(--green); flex: none; }
  .card--front .brand { left: 50%; top: 50%; transform: translate(-50%, -50%); font-size: 40px; gap: 14px; }
  .card--front .brand__dot { width: 30px; height: 30px; }
  .card--back .brand { left: 46px; top: 118px; font-size: 24px; gap: 9px; }
  .card--back .brand__dot { width: 18px; height: 18px; }

  .divider { position: absolute; left: 222px; top: 54px; width: 1px; height: 148px; background: var(--rule); }

  .holder { position: absolute; left: 248px; top: 56px; color: var(--ink); }
  .holder__name { font-size: 20px; font-weight: 700; color: var(--navy); line-height: 1.1; letter-spacing: 0.3px; }
  .holder__title { font-size: 11.5px; margin-top: 2px; }

  .contacts { position: absolute; left: 248px; top: 110px; list-style: none; color: var(--ink); font-size: 13px; }
  .contacts li { display: flex; align-items: center; gap: 10px; height: 17.5px; }
  .contacts svg { width: 12px; height: 12px; flex: none; fill: var(--green); }

  .address { position: absolute; left: 248px; top: 168px; color: var(--ink); font-size: 13px; line-height: 17.5px; font-style: normal; }

  .band-green { position: absolute; left: 0; bottom: 2px; width: 270px; height: 18px; background: var(--green); }
  .band-navy { position: absolute; right: 0; bottom: 0; width: 270px; height: 39px; background: var(--navy);
    clip-path: polygon(22px 0, 100% 0, 100% 100%, 0 100%); }
  .website { position: absolute; left: 248px; bottom: 11px; color: #fff; font-size: 13px; }
</style>
</head>
<body>
<main class="canvas">
  <section class="card card--front" aria-label="Card front">
    <div class="brand"><span class="brand__dot"></span><span>Stride DME</span></div>
  </section>

  <section class="card card--back" aria-label="Card back">
    <div class="brand"><span class="brand__dot"></span><span>Stride DME</span></div>
    <div class="divider"></div>

    <div class="holder">
      <div class="holder__name">John Smith</div>
      <div class="holder__title">Managing Director</div>
    </div>

    <ul class="contacts">
      <li>
        <svg viewBox="0 0 12 12"><rect x="2.5" y="0" width="7" height="12" rx="1.2"/><rect x="4" y="1.5" width="4" height="7" fill="#f7f7f6"/></svg>
        <span>+111 222 3333</span>
      </li>
      <li>
        <svg viewBox="0 0 12 12"><path d="M0 4 Q6 0 12 4 L10.5 5.5 L8.5 4.5 L8.5 3.5 Q6 2.8 3.5 3.5 L3.5 4.5 L1.5 5.5 Z"/><rect x="2" y="6.5" width="8" height="5" rx="1"/></svg>
        <span>+444 555 6666</span>
      </li>
      <li>
        <svg viewBox="0 0 12 12"><rect x="0" y="2" width="12" height="8"/><path d="M0.5 2.5 L6 6.5 L11.5 2.5" stroke="#f7f7f6" stroke-width="1.2" fill="none"/></svg>
        <span>yourname@yourwebsite.com</span>
      </li>
    </ul>

    <address class="address">3790 Street No.123<br>Pasadena California 99999</address>

    <div class="band-green"></div>
    <div class="band-navy"></div>
    <div class="website">www.yourwebsite.com</div>
  </section>
</main>
</body>
</html>
```